Business Card Design Project for an English Teacher

I need a business card design for my new job.
I'd like to start teaching English as a freelance.
My students will be children, teenager, and adults, who don't like or hesitate to study English and I would like to open a door to the new world for them.

I'd like to put the information below;
[right side]
1. name
2. mail address
3. mobile number
4. website or facebook page

[back]
1.my message: Feel free at asking me anything about my classes

2.lesson list such as:
price: 3150 yen ~

calsses:
kids class( mum& dad can join) ... 30 minutes / 45 minutes
students (over age 13).... 60minutes / 90 minutes
Adult (over age 19) .... 60 minutes / 90 minutes

3. I'll have both Web Lesson and Face to Face Lesson

4. Free trial lesson

Target Market(s)

My students will be children, teenager, and adults, who don't like or hesitate to study English

Industry/Entity Type

Business

Requirements
Must have
• designed both side

```html
<!DOCTYPE html>
<html lang="en">
<head>
<meta charset="utf-8">
<title>Haruka Mori – English Instructor Business Card</title>
<link rel="stylesheet" href="https://fonts.googleapis.com/css2?family=Open+Sans:wght@400;600&family=Lora:ital@1&display=swap">
<style>
  :root {
    --green: #2e9a36;
    --green-light: #4cb550;
    --green-dark: #25862c;
    --white: #ffffff;
    --ink: #222222;
    --stage: #d9d9d9;
    --faint: rgba(0,0,0,0.12);
  }
  * { margin: 0; padding: 0; box-sizing: border-box; }
  html, body { width: 1200px; height: 802px; overflow: hidden; }
  body {
    background: var(--stage);
    font-family: "Open Sans", Arial, sans-serif;
    position: relative;
  }
  .card {
    position: absolute;
    top: 240px;
    width: 530px;
    height: 321px;
    overflow: hidden;
    background: var(--white);
  }
  .card-back { left: 50px; background: linear-gradient(120deg, var(--green-dark), var(--green-light)); }
  .card-front { left: 620px; }
  .card svg.shape { position: absolute; inset: 0; }

  .vertical-label {
    position: absolute;
    writing-mode: vertical-rl;
    font-size: 21px;
    letter-spacing: 1px;
    text-transform: uppercase;
  }

  /* Front */
  .card-front .vertical-label { left: 14px; top: 20px; color: rgba(255,255,255,0.35); transform: rotate(180deg); writing-mode: vertical-lr; }
  .identity { position: absolute; left: 300px; top: 118px; color: var(--green); }
  .identity .name { font-size: 34px; font-weight: 400; line-height: 1.1; }
  .identity .role { font-size: 14px; margin-top: 2px; }
  .contact { position: absolute; left: 232px; top: 232px; font-size: 13px; color: var(--ink); }
  .contact li { list-style: none; display: flex; align-items: center; gap: 7px; line-height: 20px; }
  .contact svg { width: 12px; height: 12px; }

  /* Back */
  .back-text { position: absolute; left: 26px; top: 22px; color: var(--white); font-size: 12.5px; line-height: 1.35; }
  .back-text .message { font-family: "Lora", Georgia, serif; font-style: italic; font-size: 17px; }
  .back-text .price { font-weight: 600; }
  .back-text .classes { margin-top: 12px; }
  .back-text .lesson-modes { margin-top: 14px; }
  .back-text .trial { margin-top: 14px; font-size: 15px; }
  .card-back .vertical-label { right: 30px; bottom: 12px; color: var(--faint); transform: rotate(180deg); writing-mode: vertical-lr; font-size: 20px; }
</style>
</head>
<body>

<section class="card card-back">
  <svg class="shape" viewBox="0 0 530 321" aria-hidden="true">
    <path d="M245 321 V296 Q245 280 262 276 L530 214 V321 Z" fill="#ffffff"/>
  </svg>
  <div class="back-text">
    <p class="message">Feel free at asking me anything about my classes</p>
    <p class="price">Price: 3150 yen ~</p>
    <div class="classes">
      <p>Calsses:</p>
      <p>Kids Class (mum &amp; dad can join) ... 30 minutes / 45 minutes</p>
      <p>Students (over age 13)... 60minutes / 90 minutes</p>
      <p>Adult (over age 19) .... 60 minutes / 90 minutes</p>
    </div>
    <p class="lesson-modes">I'll have both Web Lesson and Face to Face Lesson</p>
    <p class="trial">Free trial lesson</p>
  </div>
  <span class="vertical-label">English Classes</span>
</section>

<section class="card card-front">
  <svg class="shape" viewBox="0 0 530 321" aria-hidden="true">
    <path d="M0 0 H168 L112 268 Q106 292 82 292 H0 Z" fill="#2e9a36"/>
  </svg>
  <span class="vertical-label">English Classes</span>
  <div class="identity">
    <h1 class="name">Haruka Mori</h1>
    <p class="role">English Instructor</p>
  </div>
  <ul class="contact">
    <li>
      <svg viewBox="0 0 12 12" aria-hidden="true"><circle cx="6" cy="6" r="5.2" fill="none" stroke="#555" stroke-width="1"/><path d="M4 3.2 L5 3 L5.6 4.6 L5 5.1 Q5.6 6.5 6.9 7 L7.4 6.4 L9 7 L8.8 8 Q6.5 8.6 4.6 6.6 Q3.4 5 4 3.2 Z" fill="#555"/></svg>
      090-5678-4321
    </li>
    <li>
      <svg viewBox="0 0 12 12" aria-hidden="true"><rect x="1" y="2.5" width="10" height="7" fill="#777"/><path d="M1 2.5 L6 6.5 L11 2.5" fill="none" stroke="#fff" stroke-width="0.8"/></svg>
      haruka@mailbox.jp
    </li>
  </ul>
</section>

</body>
</html>
```